Vela Stewardship Business Card design

We need a creative business card design for our hospitality management company
We need the following information:
Our business Logo: Vela Stewardship
Name: Mara Dobrinsky
Phone number: 0458 317 642
Email: mara@velastewardship.com.au
Address: 214/53 Penrose Street, Carrow Vale 3284
Web: www.velastewardship.com.au
I need the design to be a working file so that I can insert the names and numbers of the other staff members of our business.
The cards need to be 90 x 40mm
Thanks
Industry/Entity Type
Hospitality
Look and feel

```html
<!DOCTYPE html>
<html lang="en">
<head>
<meta charset="utf-8">
<title>Vela Stewardship – Business Card</title>
<link rel="stylesheet" href="https://fonts.googleapis.com/css2?family=Oswald:wght@500;700&family=Roboto+Condensed:wght@400;700&display=swap">
<style>
  :root {
    --backdrop: #8f8f8b;
    --orange-light: #f6ab1f;
    --orange-deep: #ea8905;
    --ink: #222222;
    --card-black: #1a1a1a;
    --card-black-edge: #0d0d0d;
    --band-yellow: #e7b414;
    --accent-orange: #f39a0c;
    --text-light: #e6e6e6;
  }
  * { box-sizing: border-box; margin: 0; padding: 0; }
  html, body { width: 1200px; height: 774px; overflow: hidden; }
  body {
    background: var(--backdrop);
    font-family: "Roboto Condensed", Arial, sans-serif;
    position: relative;
  }
  .card {
    position: absolute;
    width: 540px;
    height: 310px;
    border-radius: 3px;
    box-shadow: 0 14px 30px rgba(0,0,0,0.35);
    overflow: hidden;
  }
  /* Front */
  .card--front {
    left: 40px; top: 232px;
    background: radial-gradient(ellipse at 45% 35%, var(--orange-light), var(--orange-deep) 85%);
  }
  .front__brand {
    position: absolute; left: 0; right: 0; top: 92px;
    display: flex; align-items: center; justify-content: center; gap: 16px;
  }
  .brand-square {
    width: 40px; height: 40px;
    background: var(--ink);
  }
  .brand-name {
    font-family: "Oswald", Impact, sans-serif;
    font-weight: 700;
    font-size: 46px;
    letter-spacing: 0.5px;
    text-transform: uppercase;
    color: var(--ink);
    line-height: 1;
    white-space: nowrap;
  }
  .front__rule {
    position: absolute; left: 110px; right: 110px; top: 206px; height: 2px;
    background: linear-gradient(90deg, transparent, rgba(0,0,0,0.55) 30%, rgba(0,0,0,0.55) 70%, transparent);
  }
  .front__web {
    position: absolute; left: 0; right: 0; top: 222px;
    text-align: center;
    font-size: 16px; letter-spacing: 0.6px;
    color: var(--ink);
  }
  .front__web strong { font-weight: 700; }

  /* Back */
  .card--back {
    left: 620px; top: 232px;
    background: linear-gradient(160deg, #262626, var(--card-black) 50%, var(--card-black-edge));
    color: var(--text-light);
  }
  .back__brand {
    position: absolute; right: 34px; top: 48px;
    display: flex; align-items: center; gap: 10px;
  }
  .back__brand .brand-square { width: 26px; height: 26px; background: var(--accent-orange); }
  .back__brand .brand-name { font-size: 28px; color: var(--accent-orange); }
  .back__band {
    position: absolute; left: 0; right: 0; top: 112px; height: 34px;
    background: linear-gradient(90deg, var(--band-yellow) 0%, var(--band-yellow) 45%, rgba(231,180,20,0) 100%);
  }
  .back__name {
    position: absolute; left: 30px; top: 114px;
    font-weight: 700; font-size: 22px; color: var(--ink);
  }
  .contact-list {
    position: absolute; left: 30px; top: 168px;
    list-style: none;
    font-size: 16px; line-height: 28px;
  }
  .contact-list li { display: flex; align-items: center; gap: 10px; }
  .icon { width: 14px; height: 14px; flex: none; fill: var(--accent-orange); }
  .back__address {
    position: absolute; left: 300px; top: 196px;
    display: flex; gap: 10px; align-items: flex-start;
    font-style: normal; font-size: 16px; line-height: 22px;
  }
  .back__address .icon { margin-top: 3px; }
</style>
</head>
<body>
  <section class="card card--front" aria-label="Card front">
    <div class="front__brand">
      <span class="brand-square"></span>
      <span class="brand-name">Vela Stewardship</span>
    </div>
    <div class="front__rule"></div>
    <p class="front__web">www.<strong>velastewardship</strong>.com.au</p>
  </section>

  <section class="card card--back" aria-label="Card back">
    <div class="back__brand">
      <span class="brand-square"></span>
      <span class="brand-name">Vela Stewardship</span>
    </div>
    <div class="back__band"></div>
    <h1 class="back__name">Mara Dobrinsky</h1>
    <ul class="contact-list">
      <li>
        <svg class="icon" viewBox="0 0 14 14" aria-hidden="true"><rect x="3" y="0" width="8" height="14" rx="1.5"/><rect x="4.5" y="2" width="5" height="7" fill="#1a1a1a"/></svg>
        0458 317 642
      </li>
      <li>
        <svg class="icon" viewBox="0 0 14 14" aria-hidden="true"><rect x="0" y="2" width="14" height="10" rx="1"/><path d="M1 3 L7 8 L13 3" fill="none" stroke="#1a1a1a" stroke-width="1.3"/></svg>
        mara@velastewardship.com.au
      </li>
    </ul>
    <address class="back__address">
      <svg class="icon" viewBox="0 0 14 14" aria-hidden="true"><path d="M7 0 L14 7 L12 7 L12 14 L8.5 14 L8.5 10 L5.5 10 L5.5 14 L2 14 L2 7 L0 7 Z"/></svg>
      <span>214/53 Penrose Street,<br>Carrow Vale 3284</span>
    </address>
  </section>
</body>
</html>
```